Web Design Project: Need three pages designed, all for same site

Hello,

I am creating a new website that needs a clean, professional look. I need three of the pages designed for the site- all three will have the same header and footer, same brand, same top menu. These three pages represent three unique pages and unique functionality that will allow me to map out the website and then come back here and post a job for the rest of the pages.

The three pages are the Home page, the Profile Page, and the Results page.

I want an extremely simple design for these pages- my goal is for these pages to be rendered almost entirely in "code" with absolute minimal graphics- so use square corners instead of rounded ones, and simple graphic design elements that can be encoded are required.

I need a completely uncompressed PSD file of each of these pages. I want a fixed width site, with some sort of background that looks like a slight gradient up to the edge of the site to make a nice impact on the screen- look at www.plorvex.net for an example of what I am talking about. Also- the visible page should be the same width as that site.

Besides the background edge gradient framing the outside of the site, I would prefer if the only graphical elements are the site logo and a couple of small open-source icons for email and expansion with a "plus" symbol. A background image may be alright if the design is really good and the image is small so it can be quickly loaded.

I want very clean design, very simple. I will have these pages converted to HTML by a separate group.

One Bar Ad Placeholder should be located on every page in a common placement at the top- 728 by 90

Links that should be included in the main navigation bar at the top of the pages:

1. Home
2. About Us
3. Attorney Information
4. Medical Providers- Click Here To List Your Office For Free!

The Medical Providers link should be made to stand out- that is the call to action for medical providers to sign up on the site.

Other links that should be accounted for on all pages:

Login button
Username: (input field)
Password: (input field)
Forgot Login Info?
Create Account
Contact Us
Privacy Policy
Quillbook Like
Zarnix +
Hooked-Up logo
Chirpel

Requirements for each individual page:

Home Page:

This will be the home page for the site. It will contain all of the links off of it for the main site menu and navigation elements placed here will appear throughout the site. It will also have a login function at the top right and a logo in the top left.

It will have a search function dominating the left side of the home page consisting of two search input areas:

1. An open search field bar with a Sentence "Open Search by Category and city, or Provider Name: (search input field)"

2. A search panel with address, city, state, zip and two categories of drop down search screening.

The right side of the page will have a placeholder for a vidmora introduction video and some basic instructions above and below it.

Essentially, the home page is an introduction to the site and an immediate call to action to use the site for what it is intended to be used for- searching for doctors.

Profile Page:

This will be a page that is used to show the profile of the provider that has been selected. This page must be a format that can be used with all providers listed, no matter how much information each chooses to list. I want a clean appearance and placeholder text will be used to show the placement of various elements on the page. This page will be automatically generated by each provider's information with the same layout for all providers. The information included in the design should be:

Logo
Office name and specialty
Location addresses
Billing Address
Photographs of doctors with their name and specialty
Review average with number of reviews, date of oldest review, and average rating.
Individual Reviews with star rating and synopsis

Results Page:

This is a grid to display four account types as they will be listed- simple page-wide results bars displaying listings, like any search-results driven site. Each result will be clickable to expand it and show more information, so each entry on the page will need to be designed both as closed and the open panel position showing more information. Each result will build on the lesser one before it. This design will be converted to a grid that will be rendered in code, so they should be fairly simple.

That's it.

I am not looking for some complex design, or some loud website layout. I want a simple, functional, clean and professional website for my company. I will want this design to be converted to HTML code, so remember- use fonts that are common to the web. Professional, clean layout is the key here.

I will attach a logo file that you can download in AI 4 format. I do not want it altered.

I will also attach a list of menu items for the menu bar and links that will need to be on every page. For now, simply use placeholder words for them.

I added the links and menu items I need on all pages to make the top navigation and bottom footer.  

Target Market(s)

Attorneys and their clients

Industry/Entity Type

Graphic Design

Requirements
Must have
• Clear usability

```html
<!DOCTYPE html>
<html lang="en">
<head>
<meta charset="utf-8">
<title>CareLien – Home</title>
<link href="https://fonts.googleapis.com/css2?family=Arimo:wght@400;700&display=swap" rel="stylesheet">
<style>
:root{
  --blue:#2a6fb5;
  --blue-dark:#1f5c9c;
  --orange:#f15a24;
  --coral:#f0694a;
  --ink:#333;
  --muted:#555;
  --pale:#e8f0f8;
  --line:#c9d3dd;
  --peach:#e8b9a2;
  --grey:#e4e4e4;
}
*{box-sizing:border-box;margin:0;padding:0}
html,body{width:1200px;height:1089px;overflow:hidden}
body{font-family:Arimo,Arial,sans-serif;color:var(--ink);
  background:radial-gradient(ellipse at 50% 40%,#fafbfc 0%,#eef0f2 60%,#dfe3e7 100%);position:relative}
.topbar{position:absolute;top:0;left:0;right:0;height:9px;background:var(--blue)}
.page{position:absolute;left:189px;top:19px;width:823px;height:1037px;background:#fff;box-shadow:0 0 14px rgba(0,0,0,.18)}
.header{position:absolute;left:0;top:0;width:100%;height:95px;background:var(--pale)}
.tagline{position:absolute;left:9px;top:16px;width:345px;font-size:11px;line-height:14px;color:var(--orange);padding-left:15px}
.tagline .q{position:absolute;color:var(--blue);font-size:16px;font-weight:700}
.login{position:absolute;left:368px;top:10px;width:445px;height:75px;background:#fff;border:1px solid var(--line)}
.login-head{height:30px;background:var(--peach);display:flex;align-items:center;justify-content:space-between;padding:0 9px 0 12px}
.login-head strong{font-size:12.5px;color:#333;display:flex;align-items:center;gap:8px}
.login-head span{font-size:10.5px;color:#4a3a33}
.login-row{display:flex;gap:6px;padding:9px 7px 0}
.field{height:26px;border:1px solid var(--line);font-size:10.5px;padding:0 8px;display:flex;align-items:center;color:#333;background:#fff}
.btn{height:26px;background:linear-gradient(#f0f7fb,#d5e8f1);border:1px solid #a8c6d8;color:var(--blue-dark);font-size:10.5px;display:flex;align-items:center;justify-content:center}
.logo{position:absolute;left:10px;top:112px;font-size:27px;color:var(--blue-dark);display:flex;align-items:center;gap:6px;letter-spacing:-.5px}
.logo i{width:12px;height:12px;background:var(--blue-dark);border-radius:50%;display:block}
.ad{position:absolute;left:189px;top:105px;width:624px;height:81px;border:1px solid var(--line);
  background:linear-gradient(90deg,#ffffff 0%,#e4f5fb 35%,#7fd2ea 75%,#159ec7 100%);display:flex;align-items:center;padding:0 10px}
.ad-name{width:130px;font-size:15px;font-weight:700;color:#222;line-height:18px}
.ad-name small{display:block;font-size:9px;font-weight:400;color:#444}
.ad-copy{flex:1;text-align:center;font-size:19px;font-weight:700;color:#111;line-height:24px}
.ad-cta{width:110px;height:52px;border:1px solid #b6e6f4;background:#1aa6d0;color:#fff;font-size:18px;text-align:center;line-height:22px;padding-top:4px}
.ad-label{position:absolute;right:11px;top:190px;font-size:10px;font-weight:700;color:#111}
.social{position:absolute;right:11px;top:208px;height:30px;background:#dfe9f2;display:flex;align-items:center;gap:4px;padding:0 5px}
.social span{font-size:7.5px;color:#fff;background:var(--blue);padding:5px 3px;white-space:nowrap}
.nav{position:absolute;left:9px;top:250px;width:530px;height:38px;background:var(--blue);display:flex}
.nav a{color:#fff;font-size:11px;font-weight:700;text-decoration:none;display:flex;align-items:center;padding:0 15px}
.nav a.active{background:#333;padding:0 15px}
.cta{position:absolute;left:547px;top:250px;width:266px;height:38px;background:var(--coral);color:#fff;text-align:center}
.cta b{display:block;font-size:17px;line-height:19px;padding-top:3px}
.cta small{display:block;font-size:10px;font-weight:700}
.search{position:absolute;left:9px;top:297px;width:804px;height:248px;border:1px solid var(--line);padding:0 17px}
.label{font-size:12px;font-weight:700;color:var(--blue);position:absolute;left:17px}
.search .field{position:absolute;font-size:12px;color:#444;padding:0 12px;height:28px}
.select{position:absolute;height:28px;border:1px solid var(--line)}
.select::after{content:"";position:absolute;right:0;top:0;width:29px;height:100%;border-left:1px solid var(--line);background:#eef3f7}
.select svg{position:absolute;right:9px;top:10px;z-index:1}
.info{position:absolute;left:9px;top:562px;width:248px;height:338px;background:var(--pale);padding:0 10px}
.info h2{font-size:13px;text-align:center;color:#333;padding:13px 0 9px;border-bottom:6px double var(--blue)}
.info p{font-size:10.6px;line-height:17px;color:#444;text-align:justify;margin-top:11px}
.video{position:absolute;left:263px;top:562px;width:549px;height:338px;background:linear-gradient(#f4f4f4 0%,#e9e9e9 18%,#d8413a 26%,#b9302c 60%,#2a2a2a 100%)}
.video-bar{position:absolute;left:0;bottom:0;width:100%;height:26px;background:#1c1c1c;display:flex;align-items:center;gap:12px;padding:0 14px;color:#ccc;font-size:9px}
.video-bar .time b{color:#8ec8ff;font-weight:400}
.footer{position:absolute;left:0;top:926px;width:100%;height:111px;background:var(--grey);text-align:center;font-size:11px;color:#444}
.footer .links{padding-top:22px;height:47px;border-bottom:1px solid #cfcfcf}
.footer .legal{padding-top:14px;line-height:20px}
</style>
</head>
<body>
<div class="topbar"></div>
<div class="page">
  <header class="header">
    <p class="tagline"><span class="q" style="left:0;top:-4px">“</span>CareLien is the Nationwide Online Directory Of Doctors and Medical Providers that Provide Services on a Lien or Letter of Protection. <span class="q" style="position:relative">”</span></p>
    <form class="login">
      <div class="login-head"><strong><svg width="14" height="14" viewBox="0 0 14 14"><circle cx="5" cy="5" r="3.5" fill="none" stroke="#555" stroke-width="2"/><path d="M7.5 7.5L13 13" stroke="#555" stroke-width="2.4"/></svg>Please Login</strong><span>Forgot User Name or Password? Click here</span></div>
      <div class="login-row">
        <div class="field" style="width:165px">Enter User Name</div>
        <div class="field" style="width:163px">Enter Password</div>
        <div class="btn" style="width:86px;margin-left:4px">LOGIN</div>
      </div>
    </form>
  </header>

  <div class="logo"><i></i>CareLien</div>
  <div class="ad">
    <div class="ad-name">Plorvex<br>Summit<small>conference &amp; expo 2012</small></div>
    <div class="ad-copy">BRING TOGETHER MORE TALENT ON<br>ONE STAGE...</div>
    <div class="ad-cta">REGISTER<br>NOW!</div>
  </div>
  <div class="ad-label">Advertisement</div>
  <div class="social"><span>Quillbook</span><span>Chirpel</span><span>Feedwell</span><span>Hooked-Up</span><span>Zarnix +</span></div>

  <nav class="nav">
    <a class="active">HOME</a><a>ABOUT US</a><a>ATTORNEY INFORMATION</a><a>CONTACT US</a><a>CREATE ACCOUNT</a>
  </nav>
  <div class="cta"><b>MEDICAL PROVIDERS</b><small>CLICK HERE TO LIST YOUR OFFICE FOR FREE!</small></div>

  <section class="search">
    <div class="label" style="top:13px">QUICK SEARCH:</div>
    <div class="field" style="left:17px;top:33px;width:593px">Open Search by Category and city, or Provider Name:</div>
    <div class="label" style="top:79px">ADDRESS SEARCH:</div>
    <div class="field" style="left:17px;top:97px;width:200px">Enter City</div>
    <div class="select" style="left:224px;top:97px;width:208px"><svg width="11" height="7" viewBox="0 0 11 7"><path d="M0 0h11L5.5 7z" fill="#5d7a93"/></svg></div>
    <div class="field" style="left:17px;top:133px;width:200px">Enter State</div>
    <div class="field" style="left:224px;top:133px;width:208px">Enter Zip</div>
    <div class="label" style="top:181px">SCREEN BY MEDICAL PROVIDER NETWORK:</div>
    <div class="select" style="left:17px;top:199px;width:593px"><svg width="11" height="7" viewBox="0 0 11 7"><path d="M0 0h11L5.5 7z" fill="#5d7a93"/></svg></div>
    <div class="btn" style="position:absolute;left:636px;top:198px;width:128px;height:30px">SEARCH</div>
  </section>

  <aside class="info">
    <h2>WHAT YOU NEED TO KNOW?</h2>
    <p>1. An open search field bar with a Sentence "Open Search by Category and city, or Provider Name: (search input field)"</p>
    <p>2. A search panel with address, city, state, zip and two categories of drop down search screening.</p>
    <p>3. The right side of the page will have a place-holder for a vidmora introduction video and some basic instructions above and below it.</p>
    <p>4. Essentially, the home page is an introduc-tion to the site and an immediate call to action to use the site for what it is intended to be used for- searching for doctors.</p>
  </aside>

  <div class="video" role="img" aria-label="Introduction video still: three panelists seated in red armchairs on a conference stage">
    <div class="video-bar">
      <svg width="9" height="10"><rect width="3" height="10" fill="#ccc"/><rect x="6" width="3" height="10" fill="#ccc"/></svg>
      <svg width="14" height="10"><path d="M0 3h3l4-3v10L3 7H0z" fill="#ccc"/></svg>
      <span class="time"><b>0:11</b> / 4:17</span>
    </div>
  </div>

  <footer class="footer">
    <div class="links">Home | About Us | Attorney Information | Contact Us | Create new account | Login | Medical Providers Click Here</div>
    <div class="legal">Privacy Policy | Site Map | Contacts | RSS<br>© 2012 CareLien, Terms of Use</div>
  </footer>
</div>
</body>
</html>
```